Brisk Hauling Stationary design

We need a new company logo for our stationary. Be creative. Most company apparel and hats are Navy blue and Light gray. Logo does not necessarily have to contain those two colors. Pictures of trees, logging equipment, log trucks, and logs are acceptable but not required. I am open to any and all designs. Logo must reflect our pride and professionalism in the East Texas Timber Industry.
Updates

Target Market(s)

Timber owners and sawmills. Adults 25 years and up

Industry/Entity Type

Industry

Font styles to use
Serif
Decorative

Requirements
Must have
• R. T. Brisk Hauling Co.
Nice to have
• Phone number: 936-555-0142
address:
PO Box 4810
Pine Hollow, TX 75999
www.rtbriskhauling.example
rtbriskhauling@mailbox.example

```html
<!DOCTYPE html>
<html lang="en">
<head>
<meta charset="utf-8">
<title>R.T. Brisk Hauling Company – Envelope Dieline</title>
<link rel="stylesheet" href="https://fonts.googleapis.com/css2?family=Roboto+Slab:wght@400;700&display=swap">
<style>
  :root {
    --navy: #13223f;
    --flap-gray: #a4a9aa;
    --cut-line: #333333;
    --fold-line: #8a8a8a;
    --address-gray: #6b6b6b;
    --paper: #ffffff;
  }
  html, body {
    margin: 0;
    padding: 0;
    width: 1200px;
    height: 1020px;
    overflow: hidden;
    background: var(--paper);
  }
  .envelope-sheet {
    display: block;
    width: 1200px;
    height: 1020px;
  }
  .cut-line { fill: none; stroke: var(--cut-line); stroke-width: 0.8; }
  .fold-line { fill: none; stroke: var(--fold-line); stroke-width: 1; stroke-dasharray: 4 3; }
  .flap-fill { fill: var(--flap-gray); }
  .notch-mark { fill: #000000; }
  .return-address {
    font-family: "Roboto Slab", serif;
    font-size: 9.5px;
    fill: var(--address-gray);
  }
  .brand-mark { fill: var(--navy); }
  .brand-name {
    font-family: "Roboto Slab", serif;
    font-weight: 700;
    fill: var(--navy);
  }
  .preview-guide { fill: none; stroke: #b5b5b5; stroke-width: 0.8; }
</style>
</head>
<body>
<svg class="envelope-sheet" viewBox="0 0 1200 1020" xmlns="http://www.w3.org/2000/svg" role="img" aria-label="Envelope dieline for R.T. Brisk Hauling Company">

  <!-- Top closing flap -->
  <path class="flap-fill" d="M316 348 L330 316 Q334 310 342 308 L530 250 Q600 232 670 250 L858 308 Q868 312 872 320 L884 348 Z"/>
  <g class="flap-brand" transform="rotate(180 588 300)">
    <rect class="brand-mark" x="500" y="283" width="32" height="32" rx="4"/>
    <text class="brand-name" x="540" y="306" font-size="24" textLength="134" lengthAdjust="spacingAndGlyphs">R.T. BRISK</text>
    <text class="brand-name" x="541" y="318" font-size="9" textLength="130" lengthAdjust="spacingAndGlyphs">HAULING COMPANY</text>
  </g>

  <!-- Side flaps -->
  <path class="cut-line" d="M316 348 L132 406 Q114 414 114 428 Q114 438 122 446 L268 578 Q284 592 316 596"/>
  <path class="cut-line" d="M884 348 L1068 406 Q1086 414 1086 428 Q1086 438 1078 446 L932 578 Q916 592 884 596"/>

  <!-- Bottom flap -->
  <path class="cut-line" d="M316 596 Q318 612 326 620 L480 770 Q486 776 496 776 L706 776 Q714 776 720 770 L874 620 Q882 612 884 596"/>

  <!-- Front panel fold lines -->
  <rect class="fold-line" x="316" y="348" width="568" height="248"/>

  <!-- Registration notches -->
  <path class="notch-mark" d="M306 340 L314 344 L310 348 Z"/>
  <path class="notch-mark" d="M894 340 L886 344 L890 348 Z"/>
  <path class="notch-mark" d="M306 604 L314 600 L310 596 Z"/>
  <path class="notch-mark" d="M894 604 L886 600 L890 596 Z"/>

  <!-- Return address -->
  <text class="return-address" x="368" y="405">
    <tspan x="368" dy="0">PO Box 4810</tspan>
    <tspan x="368" dy="10.3">Pine Hollow, TX 75999</tspan>
    <tspan x="368" dy="10.3">www.rtbriskhauling.example</tspan>
    <tspan x="368" dy="10.3">rtbriskhauling@mailbox.example</tspan>
    <tspan x="368" dy="10.3">Phone: 936-555-0142</tspan>
  </text>

  <!-- Front brand -->
  <g class="front-brand">
    <rect class="brand-mark" x="642" y="527" width="38" height="38" rx="5"/>
    <text class="brand-name" x="697" y="551" font-size="28" textLength="158" lengthAdjust="spacingAndGlyphs">R.T. BRISK</text>
    <text class="brand-name" x="698" y="564" font-size="10.5" textLength="155" lengthAdjust="spacingAndGlyphs">HAULING COMPANY</text>
  </g>

  <!-- Folded preview -->
  <g class="folded-preview">
    <rect class="fold-line" x="855" y="851" width="307" height="132" stroke-width="0.8"/>
    <path class="preview-guide" d="M940 894 L862 966 Q856 974 857 982"/>
    <path class="preview-guide" d="M1078 894 L1154 966 Q1160 974 1160 982"/>
    <path class="flap-fill" d="M855 851 L1162 851 L1156 866 Q1154 870 1148 872 L1050 900 Q1008 912 966 900 L868 872 Q862 870 860 866 Z"/>
    <rect class="brand-mark" x="955" y="865" width="24" height="21" rx="3"/>
    <text class="brand-name" x="985" y="879" font-size="15" textLength="82" lengthAdjust="spacingAndGlyphs">R.T. BRISK</text>
    <text class="brand-name" x="985" y="886" font-size="6" textLength="81" lengthAdjust="spacingAndGlyphs">HAULING COMPANY</text>
  </g>
</svg>
</body>
</html>
```